I need a cover designed for a leadership book to fit my brand of my podcast, Ask the Dispensary Desk, www.dosageharborhub.com, with blues and greens and a professional look since it will be for a professional audience of pharmacists.

Some ideas for an image for the cover might be a woman's hand holding a compass with a road, but I welcome other ideas.

Title of the book is
"Where Chemists Steer: Voices from Women [on the Rise] Who Are Guiding, Thriving, and Reshaping Dispensing"

```html
<!DOCTYPE html>
<html lang="en">
<head>
<meta charset="UTF-8">
<title>Where Chemists Steer – Book Cover</title>
<link href="https://fonts.googleapis.com/css2?family=Oswald:wght@500;600;700&family=Nunito:wght@600&display=swap" rel="stylesheet">
<style>
  :root {
    --teal-light: #86d8d4;
    --teal-mid: #74cbc8;
    --teal-deep: #5fb9b6;
    --slate: #3e566b;
    --navy: #1b1c4b;
    --ink: #16213e;
    --scene-dark: #4d6274;
    --scene-mid: #6f8797;
  }
  * { box-sizing: border-box; margin: 0; padding: 0; }
  html, body {
    width: 886px;
    height: 1200px;
    overflow: hidden;
    background: var(--teal-mid);
  }
  .cover {
    position: relative;
    width: 886px;
    height: 1200px;
    background: linear-gradient(160deg, var(--teal-light) 0%, var(--teal-mid) 55%, var(--teal-deep) 100%);
    text-align: center;
    font-family: "Oswald", sans-serif;
  }
  .title-kicker {
    position: absolute;
    top: 95px;
    left: 0;
    width: 100%;
    font-size: 96px;
    font-weight: 600;
    line-height: 1;
    color: var(--slate);
    letter-spacing: 1px;
  }
  .title-main {
    position: absolute;
    top: 205px;
    left: 0;
    width: 100%;
    font-size: 150px;
    font-weight: 600;
    line-height: 1;
    color: var(--navy);
    letter-spacing: 1px;
  }
  .title-verb {
    position: absolute;
    top: 345px;
    left: 0;
    width: 100%;
    font-size: 310px;
    font-weight: 700;
    line-height: 1;
    color: var(--slate);
    letter-spacing: 4px;
  }
  .cover-illustration {
    position: absolute;
    top: 700px;
    left: 193px;
    width: 500px;
    height: 215px;
    border-radius: 50%;
    background: radial-gradient(ellipse at 50% 55%, var(--scene-mid) 0%, var(--scene-dark) 60%, rgba(77, 98, 116, 0) 72%);
  }
  .subtitle {
    position: absolute;
    top: 935px;
    left: 90px;
    width: 706px;
    font-family: "Nunito", sans-serif;
    font-weight: 600;
    font-size: 38px;
    line-height: 1.3;
    color: var(--ink);
  }
  .author {
    position: absolute;
    top: 1090px;
    left: 0;
    width: 100%;
    font-size: 54px;
    font-weight: 600;
    line-height: 1;
    color: var(--navy);
    letter-spacing: 1px;
  }
</style>
</head>
<body>
  <main class="cover">
    <h1 class="book-title">
      <span class="title-kicker">WHERE</span>
      <span class="title-main">CHEMISTS</span>
      <span class="title-verb">STEER</span>
    </h1>
    <div class="cover-illustration" role="img" aria-label="Illustration of a businesswoman standing on a large compass dial with a red and blue needle"></div>
    <p class="subtitle">Voices from Women [on the Rise] Who Are Guiding, Thriving, and Reshaping Dispensing</p>
    <p class="author">DR. MAREN HOLLOWAY, PHARMD</p>
  </main>
</body>
</html>
```